Vantorq, Business Intelligence Consultant Web Design

We need a web design for a Business Intelligence Consultant Enterprise.
We design, develop and mantain management systems and reports that delivered to the final user a complete information about their business. With that information they can take better management decisions.
Our principal service is KLV Business Intelligence proyects, using KLV Data Vault and KLV Report Suite tools.
Also we develop web systems that integrate mobile technology with KLV Systems and end user database systems.

Our principal objective is to be a partner of our clients more than a service provider, the idea is to offer a complete service to our customers that allow both companies grow togheter.

The final design must present our list of services and products, and show our experience in business intelligence projects.

Target Market(s)

Companies that runs KLV systems, Business companies, companies with production processes, retail, logistic process (inventory management)

Industry/Entity Type

Business

Requirements
Must have
• The brochure must have 4 pages:
Home
Empresa
Business Intelligence
Aplicaciones empresariales móviles
Metodología

And a contact form to receive customer contact.
- Name
- Company
- Contact Email
- Message text

For the color I will upload both company logos with different colors that u can use. Obviously you can add color if you want.
Nice to have
• The principal idea is to show to customer that all information of his business can be summarized on one graphic panel and can be consulted from any device.

Is nice to have business graphics on the web design, maybe abstract and give the idea of management information can be obtained easily.

Should not have
• Please, PLEASE!, don't use on the web site a meeting photo or people watching a business report on a lobby or some business man making a presentation.
Neither images of team building or people at the office.

That images are too used to present the business intelligence concept and the principal idea is to have information, and not people working hard to obtain that.

```html
<!DOCTYPE html>
<html lang="en">
<head>
<meta charset="utf-8">
<title>Vantorq — Business Intelligence</title>
<link rel="stylesheet" href="https://fonts.googleapis.com/css2?family=Open+Sans:wght@400;600;700&family=Poppins:wght@600&family=Carlito&family=Tinos&display=swap">
<style>
  :root{
    --header-bg:#050505;
    --nav-top:#8a8a8a;
    --nav-bottom:#3e3e3e;
    --nav-active:#c8141b;
    --brand-red:#d21f26;
    --main-bg:#5c5b60;
    --text-light:#dcdcdc;
    --text-muted:#a9a9ad;
    --white:#ffffff;
    --news-cyan:#2fc3d6;
    --news-border:#8fe0ea;
    --subscribe:#f2400f;
    --footer-bg:#1d1d1e;
    --footer-text:#9a9a9a;
  }
  *{margin:0;padding:0;box-sizing:border-box}
  html,body{width:913px;height:1200px;overflow:hidden}
  body{position:relative;background:var(--main-bg);font-family:"Open Sans",Arial,sans-serif;color:var(--text-light)}
  .abs{position:absolute}
  h1,h2,h3,h4{font-weight:400}

  /* header */
  .site-header{left:0;top:0;width:913px;height:62px;background:var(--header-bg)}
  .brand{left:108px;top:15px;display:flex;align-items:center;gap:8px}
  .brand-mark{width:28px;height:28px;background:#8c8c8c}
  .brand-name{font-family:"Open Sans",sans-serif;font-size:26px;font-weight:600;color:var(--brand-red);letter-spacing:-.3px}
  .call-line{right:194px;top:24px;font-size:10px;color:#bdbdbd;white-space:nowrap}
  .call-line strong{color:var(--white);font-weight:700;margin-left:2px}
  .social-top{left:732px;top:22px;display:flex;gap:2px}
  .social-top span{width:17px;height:17px;background:#e8e8e8;display:block}

  /* navigation */
  .main-nav{left:0;top:62px;width:913px;height:30px;background:linear-gradient(var(--nav-top),#5d5d5d 50%,var(--nav-bottom));border-top:1px solid #a9a9a9}
  .main-nav ul{list-style:none;display:flex;position:absolute;left:110px;top:0;height:30px}
  .main-nav li{height:29px;line-height:29px;padding:0 9px;font-size:11px;color:var(--white);text-transform:uppercase;border-right:1px solid #2e2e2e;box-shadow:1px 0 0 #7c7c7c;white-space:nowrap}
  .main-nav li.active{background:var(--nav-active)}

  /* hero */
  .hero{left:0;top:92px;width:913px;height:327px;background:radial-gradient(ellipse at 28% 55%,#b8875a 0%,#9a9a9a 25%,#dcdcdc 55%,#f0f0f0 80%)}
  .hero-title{left:489px;top:136px;font-family:"Poppins",sans-serif;font-weight:600;font-size:31px;line-height:32px;color:#0a0a0a;letter-spacing:-.3px}
  .hero-text{left:490px;top:221px;width:275px;font-size:10.6px;line-height:17.8px;color:#111}
  .btn-learn{left:490px;top:319px;width:113px;height:38px;background:linear-gradient(#727276,#4d4d51);border-radius:3px;box-shadow:0 2px 3px rgba(0,0,0,.4);color:#121212;font-size:13.5px;line-height:38px;text-align:center;letter-spacing:.3px}

  /* section labels */
  .label-box{height:32px;background:linear-gradient(#3a3a3c,#202021);border:1px solid #727276;border-radius:3px;color:var(--white);font-family:"Carlito",sans-serif;font-weight:400;font-size:18px;line-height:30px;padding-left:13px;box-shadow:0 1px 3px rgba(0,0,0,.4)}

  .welcome-title{left:108px;top:442px;width:187px}
  .welcome-text{left:108px;top:488px;width:462px;font-size:9.6px;line-height:14.3px;color:var(--text-light)}

  .column-divider{left:594px;top:440px;width:6px;height:440px;background:linear-gradient(90deg,rgba(0,0,0,0),rgba(0,0,0,.18),rgba(0,0,0,0))}

  /* info tabs */
  .info-panel{left:108px;top:619px;width:473px;height:158px;background:#4b4b4e;border:1px solid #3a3a3c;border-radius:4px;box-shadow:0 1px 4px rgba(0,0,0,.35);display:flex;overflow:hidden}
  .info-col{flex:1;position:relative;border-right:1px solid #58585b}
  .info-col:last-child{border-right:0}
  .info-col h3{height:30px;background:#3f3f42;font-family:"Carlito",sans-serif;font-size:14px;line-height:28px;color:var(--white);padding-left:13px}
  .info-col p{padding:7px 10px 0 13px;font-size:10px;line-height:15px;color:var(--text-light)}
  .info-col a{position:absolute;left:13px;top:126px;font-size:9px;color:var(--white);text-decoration:none}

  /* news */
  .news-title{left:110px;top:794px;font-family:"Carlito",sans-serif;font-size:16px;color:var(--white)}
  .news-item{left:110px;width:460px;display:flex;gap:7px}
  .news-thumb{width:46px;height:46px;flex:none;border:1px solid #9a9a9a}
  .news-item h4{font-size:9.5px;font-weight:700;color:var(--white);line-height:12px}
  .news-item p{font-size:9.4px;line-height:12.8px;color:var(--text-light)}

  /* testimonials */
  .testimonials-title{left:617px;top:442px;width:109px;padding-left:8px}
  .quote{left:617px;width:188px}
  .quote p{font-size:10px;line-height:12.8px;color:var(--text-light)}
  .quote .role{text-align:right;font-size:10px;color:var(--text-muted);margin-top:6px;line-height:11px}
  .quote .name{text-align:right;font-family:"Carlito",sans-serif;font-size:14px;color:var(--white);text-transform:uppercase;line-height:14px}

  /* newsletter */
  .newsletter{left:617px;top:886px;width:188px;height:130px;background:var(--news-cyan);border:2px solid var(--news-border)}
  .newsletter h3{position:absolute;left:9px;top:7px;font-family:"Tinos",serif;font-size:17px;color:var(--white);letter-spacing:.3px}
  .newsletter .mail-icon{position:absolute;left:143px;top:0;width:26px;height:22px;background:var(--white)}
  .newsletter p{position:absolute;left:9px;top:29px;width:172px;font-size:8.5px;line-height:11px;color:var(--white)}
  .newsletter label{position:absolute;left:9px;top:58px;font-size:9.5px;color:var(--white)}
  .newsletter .field{position:absolute;left:9px;top:72px;width:164px;height:20px;background:var(--white)}
  .newsletter .subscribe{position:absolute;left:9px;top:100px;width:164px;height:20px;background:var(--subscribe);font-family:"Tinos",serif;font-size:15px;line-height:20px;text-align:center;color:var(--white)}

  /* footer */
  .site-footer{left:0;top:1066px;width:913px;height:134px;background:var(--footer-bg);border-top:1px solid #111}
  .footer-heading{font-family:"Carlito",sans-serif;font-weight:400;font-size:14px;color:#e6e6e6}
  .footer-list{font-size:9px;line-height:13px;color:var(--footer-text)}
  .footer-links{left:645px;top:1087px;font-size:10px;color:var(--footer-text);letter-spacing:.3px}
  .footer-links span{margin:0 6px}
  .footer-rule{height:1px;background:#343435}
  .stay-label{left:634px;top:1130px;font-size:10px;color:var(--footer-text);letter-spacing:.3px}
  .social-dot{width:22px;height:22px;border-radius:50%;background:#5a5a5b;top:1125px}
  .copyright{left:108px;top:1179px;font-size:8.6px;color:#bdbdbd}
</style>
</head>
<body>

<header class="site-header abs">
  <div class="brand abs">
    <span class="brand-mark"></span>
    <span class="brand-name">vantorq</span>
  </div>
  <div class="call-line abs">For additional information call: <strong>+00 1300 2214</strong></div>
  <div class="social-top abs" aria-label="Social links"><span></span><span></span><span></span><span></span></div>
</header>

<nav class="main-nav abs">
  <ul>
    <li class="active">Home</li>
    <li>Empresa</li>
    <li>Business Intelligence</li>
    <li>Aplicaciones empresariales móviles</li>
    <li>Metodología</li>
    <li>Contact Us</li>
  </ul>
</nav>

<section class="hero abs" role="img" aria-label="Abstract 3D arrows in copper and steel tones sweeping upward"></section>
<h1 class="hero-title abs">Lorem ipsum dolor<br>sit amet</h1>
<p class="hero-text abs">Sed ut perspiciatis unde omnis iste natus error sit voluptatem accusantium doloremque laudantium, totam rem aperiam, eaque ipsa quae ab illo inventore veritatis et quasi architecto beatae vitae dicta sunt explicabo.</p>
<div class="btn-learn abs">LEARN MORE</div>

<h2 class="label-box welcome-title abs">Welcome to vantorq</h2>
<p class="welcome-text abs">Sed ut perspiciatis unde omnis iste natus error sit voluptatem accusantium doloremque laudantium, totam rem aperiam, eaque ipsa quae ab illo inventore veritatis et quasi architecto beatae vitae dicta sunt explicabo. Nemo enim ipsam voluptatem quia voluptas sit aspernatur aut odit aut fugit, sed quia consequuntur magni dolores eos qui ratione voluptatem sequi nesciunt. Neque porro quisquam est, qui dolorem ipsum quia dolor sit amet, consectetur, adipisci velit, sed quia non numquam eius modi tempora incidunt ut labore et dolore magnam aliquam quaerat voluptatem.</p>

<div class="column-divider abs"></div>

<div class="info-panel abs">
  <div class="info-col">
    <h3>Who we are</h3>
    <p>Lorem ipsum dolor sit amet, consectetur adipisicing elit, sed do eiusmod tempor incididunt ut labore et dolore magna aliqua.</p>
    <a href="#">Get to know us better</a>
  </div>
  <div class="info-col">
    <h3>What we do</h3>
    <p>Lorem ipsum dolor sit amet, consectetur adipisicing elit, sed do eiusmod tempor incididunt ut labore et dolore magna aliqua.</p>
    <a href="#">Share our vision</a>
  </div>
  <div class="info-col">
    <h3>Why choose us</h3>
    <p>Lorem ipsum dolor sit amet, consectetur adipisicing elit, sed do eiusmod tempor incididunt ut labore et dolore magna aliqua.</p>
    <a href="#">See for yourself</a>
  </div>
</div>

<h2 class="news-title abs">News</h2>
<article class="news-item abs" style="top:823px">
  <div class="news-thumb" role="img" aria-label="Golden light trails" style="background:linear-gradient(135deg,#3a2a10,#d99a2a,#5a3a10)"></div>
  <div><h4>Heading</h4><p>Lorem ipsum dolor sit amet, consectetur adipisicing elit, sed do eiusmod tempor incididunt ut labore et dolore magna aliqua. Ut enim ad minim veniam, quis nostrud exercitation ullamco laboris nisi ut aliquip ex ea commodo consequat.</p></div>
</article>
<article class="news-item abs" style="top:891px">
  <div class="news-thumb" role="img" aria-label="Blue and orange light streaks" style="background:linear-gradient(135deg,#2a4fa8,#9fc8f0,#e0804a)"></div>
  <div><h4>Heading</h4><p>Lorem ipsum dolor sit amet, consectetur adipisicing elit, sed do eiusmod tempor incididunt ut labore et dolore magna aliqua. Ut enim ad minim veniam, quis nostrud exercitation ullamco laboris nisi ut aliquip ex ea commodo consequat.</p></div>
</article>
<article class="news-item abs" style="top:959px">
  <div class="news-thumb" role="img" aria-label="Red and violet light trails" style="background:linear-gradient(135deg,#3a2050,#c0404a,#f0a070)"></div>
  <div><h4>Heading</h4><p>Lorem ipsum dolor sit amet, consectetur adipisicing elit, sed do eiusmod tempor incididunt ut labore et dolore magna aliqua. Ut enim ad minim veniam, quis nostrud exercitation ullamco laboris nisi ut aliquip ex ea commodo consequat.</p></div>
</article>

<h2 class="label-box testimonials-title abs">Testimonials</h2>
<blockquote class="quote abs" style="top:482px">
  <p>But I must explain to you how all this mistaken idea of denouncing pleasure and praising pain was born and I will give you a complete account of the system, and expound the actual teachings</p>
  <div class="role">Director</div><div class="name">Lena Hart</div>
</blockquote>
<blockquote class="quote abs" style="top:615px">
  <p>At vero eos et accusamus et iusto odio dignissimos ducimus qui blanditiis praesentium voluptatum deleniti atque corrupti quos dolores et quas molestias excepturi sint occaecati cupiditate non provident.</p>
  <div class="role">Senior assistant</div><div class="name">Tom Varga</div>
</blockquote>
<blockquote class="quote abs" style="top:747px">
  <p>But I must explain to you how all this mistaken idea of denouncing pleasure and praising pain was born and I will give you a complete account of the system, and expound the actual teachings</p>
  <div class="role">Junior researcher</div><div class="name">Paul Denning</div>
</blockquote>

<form class="newsletter abs">
  <h3>NEWSLETTER</h3>
  <span class="mail-icon"></span>
  <p>Lorem ipsum dolor sit amet, consectet adipisic ing elit, sed do eiusmod tempor.</p>
  <label>Email Address</label>
  <div class="field"></div>
  <div class="subscribe">SUBSCRIBE NOW</div>
</form>

<footer class="site-footer abs"></footer>
<h3 class="footer-heading abs" style="left:108px;top:1086px">Contact Info</h3>
<p class="footer-list abs" style="left:108px;top:1113px">48 Harbor Lane<br>Eastvale, P.O 31207<br>T: +00 1300 2215</p>
<h3 class="footer-heading abs" style="left:273px;top:1086px">Quick Navigation</h3>
<p class="footer-list abs" style="left:276px;top:1113px">Home<br>Empresa<br>Business Intelligence</p>
<p class="footer-list abs" style="left:392px;top:1113px">Aplicaciones empresariales móviles<br>Metodología<br>Contact Us</p>
<div class="footer-links abs">EMAIL<span>|</span>Contact Us Now</div>
<div class="footer-rule abs" style="left:617px;top:1116px;width:188px"></div>
<div class="stay-label abs">STAY IN TOUCH</div>
<span class="social-dot abs" style="left:736px"></span>
<span class="social-dot abs" style="left:765px"></span>
<div class="footer-rule abs" style="left:0;top:1171px;width:913px"></div>
<p class="copyright abs">© 2011 vantorq. All right are reserved. &nbsp;Terms of service | Privacy Policy</p>

</body>
</html>
```